KM Group

We need a new website for our company and since we had a very good work done for our logo in this site, we're back for the entire job.

Our company name is Halvorsen Capital Group. We're adding files of examples of what we have done today. In my opinion we need a more attention lock in the site but yet financial simple work.

Our files (attached) will let you know what we have so far. We need a complete change but the colours should be the same, however you can change them not running away to far from the original, and of course matching with the logo.

We need examples for 3 kind of layouts.

- A HOME welcome layout
- An internal Layout with sidebar
- And internal Layout wide

We can buy image licenses if needed for assets.
Actually there are 5 slide images placed on the Welcome HOME, we need those there, but you can improve with better images to match the new website!!!

Target Market(s)

Clients looking for financial advisers, tax and funds specialist, currency advisers

Industry/Entity Type

Financial

Requirements
Must have
• all the fonts must be in accordance with the financial market sites........the welcome home page must be precise, neat and information accurate........the menu should be elegant........main focus on the Home page, should be also the PRIVATE ACCESS box log in.......

```html
<!DOCTYPE html>
<html lang="en">
<head>
<meta charset="utf-8">
<title>Halvorsen Capital Group</title>
<link href="https://fonts.googleapis.com/css2?family=Open+Sans:ital,wght@0,400;0,600;0,700;1,400&display=swap" rel="stylesheet">
<style>
:root{
  --orange:#f07a1e;
  --ink:#222;
  --text:#444;
  --rule:#999;
  --navy:#1d3557;
  --footer:#1d1d1d;
  --footer-text:#bbb;
  --card:#f4f4f4;
}
*{margin:0;padding:0;box-sizing:border-box}
html,body{width:838px;height:1200px;overflow:hidden;background:#fff}
body{position:relative;font-family:"Open Sans",Arial,sans-serif;color:var(--text)}
.abs{position:absolute}
.brand{left:94px;top:14px;display:flex;align-items:center;gap:6px}
.brand-mark{width:22px;height:22px;background:var(--orange)}
.brand-name{font-size:11px;font-weight:600;color:var(--ink);letter-spacing:.3px;line-height:1.2}
.contact{right:78px;top:16px;font-size:11px;color:#555}
.contact .sep{display:inline-block;width:1px;height:13px;background:#888;margin:0 8px;vertical-align:middle}
.nav{left:335px;top:42px;display:flex;height:28px;font-size:9.5px}
.nav a{color:#333;text-decoration:none;padding:0 12px;line-height:28px}
.nav a.active{background:var(--orange);color:#fff;padding:0 9px}
.hero{left:0;top:70px;width:838px;height:298px;
  background:
    radial-gradient(ellipse 260px 170px at 360px 140px,rgba(255,255,255,.85),rgba(255,255,255,0) 70%),
    radial-gradient(ellipse 180px 230px at 60px 200px,rgba(240,240,240,.9),rgba(240,240,240,0) 70%),
    linear-gradient(100deg,#cfcfcf 0%,#e6e6e6 25%,#bdbdbd 45%,#8f8f8f 62%,#5a5a5a 80%,#3c3c3c 100%)}
.hero-band{left:0;top:306px;width:838px;height:62px;background:rgba(40,40,40,.78)}
.hero-title{left:88px;top:311px;font-size:19px;font-weight:700;color:#fff;letter-spacing:-.3px}
.hero-sub{left:90px;top:337px;width:630px;font-size:10px;line-height:12px;color:#eee}
.h2{font-size:15px;color:var(--ink);font-weight:400}
.h2 em{font-style:normal;color:var(--orange)}
.rule{height:1px;background:var(--rule)}
.intro{left:88px;top:432px;width:440px;font-size:8.6px;line-height:15.7px;color:#333}
.readmore{left:89px;top:537px;font-size:10px;font-style:italic;color:#111}
.field{left:572px;width:170px;height:23px;border:1px solid #ccc;font-size:7px;font-style:italic;color:#666;padding:7px 8px}
.forgot{left:573px;top:501px;font-size:8.5px;font-style:italic;color:#111}
.btn{left:572px;top:526px;width:94px;height:23px;background:var(--orange);color:#fff;font-size:8.5px;font-weight:600;text-align:center;line-height:23px}
.dots{border-top:1px dotted #999}
.arrow{width:13px;height:12px;background:#eee;font-size:8px;color:#bbb;text-align:center;line-height:12px}
.card{top:626px;width:209px;height:185px;background:var(--card)}
.card-img{height:104px}
.img-team{background:radial-gradient(ellipse 90px 60px at 110px 40px,#f5f5f5,rgba(245,245,245,0) 75%),linear-gradient(180deg,#d6d6d6 0%,#8a8a8a 55%,#3e3e3e 100%)}
.img-coins{background:radial-gradient(ellipse 70px 40px at 105px 30px,#e4e4e4,rgba(228,228,228,0) 75%),linear-gradient(180deg,#bdbdbd 0%,#a3a3a3 50%,#5c5c5c 80%,#8c8c8c 100%)}
.img-globe{background:radial-gradient(circle at 100px 55px,#f0f0f0 0,#9a9a9a 45px,rgba(154,154,154,0) 62px),linear-gradient(135deg,#e2e2e2,#9e9e9e 60%,#6a6a6a)}
.card h3{text-align:center;font-size:10.5px;font-weight:400;color:#222;margin-top:17px;letter-spacing:.2px}
.card p{font-size:8px;line-height:10.8px;color:#888;padding:6px 14px 0}
.badge{top:879px;height:78px;border:3px solid #ddd;background:#fff;display:flex;align-items:center;justify-content:center}
.badge span{display:block;width:90px;height:36px;background:#d8d8d8;border-radius:4px}
.footer{left:0;top:982px;width:838px;height:218px;background:var(--footer)}
.fcol{top:1000px;font-size:10px;color:#ddd}
.fcol h4{font-weight:400;font-size:10px;margin-bottom:14px}
.fcol a{display:block;font-size:7.5px;line-height:14.6px;color:var(--footer-text);text-decoration:underline}
.copy{left:0;width:838px;top:1174px;text-align:center;font-size:7.5px;color:#aaa}
</style>
</head>
<body>
<header>
  <div class="abs brand"><span class="brand-mark"></span><span class="brand-name">HALVORSEN<br>CAPITAL GROUP</span></div>
  <div class="abs contact">contact@halvorsencapital.com<span class="sep"></span>Toll Free 800-555-0147</div>
  <nav class="abs nav"><a class="active">Home</a><a>About Us</a><a>Investments</a><a>Funds</a><a>Brokerage</a><a>Exchange</a><a>Accounts</a></nav>
</header>

<section>
  <div class="abs hero" role="img" aria-label="Black and white photo of a hand pointing at a bar chart on a tablet beside a glass"></div>
  <div class="abs hero-band"></div>
  <div class="abs hero-title">TEAM WORK FOR YOUR BENEFIT</div>
  <div class="abs hero-sub">Our dedicated Private Bankers, will proactively keep you up to date with relevant information and provide a financial overview that enables you to make good decisions</div>
</section>

<section>
  <h2 class="abs h2" style="left:88px;top:389px">Welcome to <em>HALVORSEN CAPITAL GROUP</em></h2>
  <div class="abs rule" style="left:88px;top:416px;width:433px"></div>
  <p class="abs intro">Lorem Ipsum is simply dummy text of the printing and typesetting industry. Lorem Ipsum has been the industry's standard dummy text ever since the 1500s, when an unknown printer took a galley of type and scrambled it to make a type specimen book. It has survived not only five centuries, but also the leap into electronic typesetting, remaining essentially unchanged. Lorem Ipsum is simply dummy text of the printing and typesetting industry. Lorem Ipsum has been the industry's standard dummy text ever since the 1500s, when an unknown printer took a galley of type and scrambled it to make a type.</p>
  <div class="abs readmore">--- Read More</div>

  <h2 class="abs h2" style="left:572px;top:389px">Private Access</h2>
  <div class="abs rule" style="left:572px;top:416px;width:179px"></div>
  <div class="abs field" style="top:436px">Account Number</div>
  <div class="abs field" style="top:466px">Account Password</div>
  <div class="abs forgot">Forgot account number/password?</div>
  <div class="abs btn">ACCOUNT LOGIN</div>
</section>

<section>
  <h2 class="abs h2" style="left:90px;top:574px;font-size:13.5px">Recent Projects</h2>
  <div class="abs dots" style="left:90px;top:597px;width:656px"></div>
  <div class="abs" style="left:90px;top:595px;width:100px;height:3px;background:var(--navy)"></div>
  <div class="abs arrow" style="left:719px;top:578px">&lsaquo;</div>
  <div class="abs arrow" style="left:733px;top:578px">&rsaquo;</div>

  <div class="abs card" style="left:90px"><div class="card-img img-team" role="img" aria-label="Black and white photo of a team meeting at a table"></div><h3>MANAGEMENT &amp; STRATEGY</h3><p>Lorem Ipsum is simply dummy text of the printing and typesetting industry. Lorem Ipsum has been the industry's standard dummy text</p></div>
  <div class="abs card" style="left:314px"><div class="card-img img-coins" role="img" aria-label="Black and white photo of stacks of coins"></div><h3>FUNDS</h3><p>Lorem Ipsum is simply dummy text of the printing and typesetting industry. Lorem Ipsum has been the industry's standard</p></div>
  <div class="abs card" style="left:538px"><div class="card-img img-globe" role="img" aria-label="Black and white photo of a globe with coin stacks"></div><h3>CURRENCY EXCHANGE</h3><p>Lorem Ipsum is simply dummy text of the printing and typesetting industry. Lorem Ipsum has been the industry's standard dummy text</p></div>
</section>

<section>
  <h2 class="abs h2" style="left:92px;top:829px;font-size:13.5px">Verified and Protected by</h2>
  <div class="abs dots" style="left:92px;top:853px;width:654px"></div>
  <div class="abs" style="left:92px;top:852px;width:158px;height:3px;background:var(--orange)"></div>
  <div class="abs badge" style="left:90px;width:164px"><span></span></div>
  <div class="abs badge" style="left:257px;width:163px"><span></span></div>
  <div class="abs badge" style="left:423px;width:163px"><span></span></div>
  <div class="abs badge" style="left:590px;width:156px"><span style="width:54px;height:54px;border-radius:50%"></span></div>
</section>

<footer>
  <div class="abs footer"></div>
  <div class="abs fcol" style="left:110px"><h4>About Us</h4><a>Home</a><a>Expertise</a><a>Identity</a><a>Strategy</a><a>Contact Us</a></div>
  <div class="abs fcol" style="left:223px"><h4>Investments</h4><a>Yous voulez utiliser</a><a>Passage du Lorem</a><a>Yous devez être sûr Gu'll</a><a>n'y a rien</a><a>Embarrassant caché</a><a>Dans le texte.</a><a>Générateurs de Lorem</a></div>
  <div class="abs fcol" style="left:376px"><h4>Funds</h4><a>Overview</a><a>Administration</a><a>Funds Security</a><a>Core Services</a><a>Reporting</a><a>Revenue Oppurtunities</a><a>How It Works</a><a>Glossary</a></div>
  <div class="abs fcol" style="left:518px"><h4>Currency Exchange</h4><a>Foreign Exchanfe</a><a>Exchange Forward</a><a>Exchange Options</a><h4 style="margin:8px 0 10px">Accounts</h4><a>Apply Now</a><a>Private Access</a></div>
  <div class="abs fcol" style="left:672px"><h4>Brokerage</h4><a>Institutional</a><a>Research</a><a>Trading</a></div>
  <div class="abs" style="left:79px;top:1161px;width:685px;height:1px;background:#3a3a3a"></div>
  <div class="abs copy">© Copyrights 2013 All rights Reserved</div>
</footer>
</body>
</html>
```